Valbrina Soletti Winery 2023 Label

We are just about to bottle our very first Napa Valley Cabernet Sauvignon and need label ideas

Target Market(s)

Cab drinkers who like Napa California Cabs

Industry/Entity Type

Wine Making

Logo Text

Valbrina Soletti 2023 Napa Estate Grown Cabernet Sauvignon

Requirements
Must have
• Winery Name, year of vintage and Napa Estate Cab
Nice to have
• If using the initials V and S use gold letters on black or red background

```html
<!DOCTYPE html>
<html lang="en">
<head>
<meta charset="utf-8">
<title>Valbrina Soletti Vineyards – Estate Cabernet Sauvignon 2023</title>
<link rel="stylesheet" href="https://fonts.googleapis.com/css2?family=Rye&family=Oswald:wght@500;600&display=swap">
<style>
  :root {
    --paper: #f0e0c0;
    --ink: #4a4431;
    --scene-light: #cfc09a;
    --grape: #b9ad8a;
  }
  html, body {
    margin: 0;
    width: 1200px;
    height: 1200px;
    overflow: hidden;
    background: var(--paper);
  }
  .label {
    display: block;
    width: 1200px;
    height: 1200px;
  }
  .frame-outer { fill: none; stroke: var(--ink); stroke-width: 5; stroke-linejoin: round; }
  .frame-inner { fill: none; stroke: var(--ink); stroke-width: 2; stroke-linejoin: round; }
  .rule { stroke: var(--ink); stroke-width: 2; }
  .display {
    font-family: "Rye", serif;
    fill: var(--ink);
  }
  .small-caps {
    font-family: "Oswald", sans-serif;
    font-weight: 600;
    fill: var(--ink);
    letter-spacing: 2px;
  }
  .monogram {
    font-family: "Oswald", sans-serif;
    font-weight: 500;
    fill: var(--ink);
  }
</style>
</head>
<body>
<svg class="label" viewBox="0 0 1200 1200" xmlns="http://www.w3.org/2000/svg">
  <defs>
    <path id="arch-name" d="M392,340 Q600,180 812,340"/>
    <path id="arch-vineyards" d="M465,478 Q600,440 735,478"/>
    <linearGradient id="scene-fill" x1="0" y1="0" x2="0" y2="1">
      <stop offset="0" stop-color="var(--scene-light)"/>
      <stop offset="0.55" stop-color="#8f845f"/>
      <stop offset="1" stop-color="var(--ink)"/>
    </linearGradient>
    <radialGradient id="grape-fill" cx="0.5" cy="0.45" r="0.6">
      <stop offset="0" stop-color="#d8caa3"/>
      <stop offset="1" stop-color="var(--grape)"/>
    </radialGradient>
  </defs>

  <!-- Badge frame -->
  <g class="badge-frame">
    <path class="frame-outer" d="M345,395 L345,330 Q345,200 560,160 Q592,150 600,128 Q608,150 640,160 Q878,200 878,330 L878,395 Q600,180 345,395 Z"/>
    <path class="frame-outer" d="M405,372 L405,662 L378,662 L378,895 Q470,900 530,955 M795,372 L795,662 L822,662 L822,895 Q730,900 670,955"/>
    <path class="frame-inner" d="M420,362 L420,676 L392,676 L392,880 L808,880 L808,676 L780,676 L780,362"/>
  </g>

  <!-- Winery name -->
  <text class="display" font-size="62" letter-spacing="3" text-anchor="middle">
    <textPath href="#arch-name" startOffset="50%">VALBRINA</textPath>
  </text>

  <g class="monogram-row">
    <line class="rule" x1="505" y1="318" x2="565" y2="318"/>
    <line class="rule" x1="505" y1="324" x2="565" y2="324"/>
    <line class="rule" x1="635" y1="318" x2="695" y2="318"/>
    <line class="rule" x1="635" y1="324" x2="695" y2="324"/>
    <text class="monogram" x="600" y="334" font-size="30" text-anchor="middle">VS</text>
  </g>

  <text class="display" x="600" y="395" font-size="56" text-anchor="middle" textLength="250" lengthAdjust="spacingAndGlyphs">SOLETTI</text>

  <text class="display" font-size="44" letter-spacing="1" text-anchor="middle">
    <textPath href="#arch-vineyards" startOffset="50%">VINEYARDS</textPath>
  </text>

  <!-- Vineyard scene -->
  <rect class="vineyard-scene" x="470" y="488" width="262" height="180" fill="url(#scene-fill)" role="img" aria-label="Engraved vineyard landscape: sunburst over hills, rows of vines leading to the horizon, flanked by cypress trees"/>

  <!-- Varietal block -->
  <g class="estate-line">
    <line class="rule" x1="470" y1="690" x2="548" y2="690"/>
    <line class="rule" x1="652" y1="690" x2="730" y2="690"/>
    <text class="small-caps" x="600" y="697" font-size="18" text-anchor="middle">ESTATE</text>
  </g>

  <text class="display" x="600" y="778" font-size="78" text-anchor="middle" textLength="360" lengthAdjust="spacingAndGlyphs">CABERNET</text>
  <text class="display" x="600" y="862" font-size="78" text-anchor="middle" textLength="378" lengthAdjust="spacingAndGlyphs">SAUVIGNON</text>

  <g class="appellation">
    <line class="rule" x1="470" y1="898" x2="548" y2="898"/>
    <line class="rule" x1="652" y1="898" x2="730" y2="898"/>
    <text class="small-caps" x="600" y="908" font-size="26" text-anchor="middle">NAPA</text>
    <text class="small-caps" x="600" y="938" font-size="17" text-anchor="middle">2023</text>
  </g>

  <!-- Grape cluster -->
  <ellipse class="grape-cluster" cx="600" cy="1032" rx="82" ry="74" fill="url(#grape-fill)" role="img" aria-label="Engraved grape cluster with vine leaves and tendril"/>
</svg>
</body>
</html>
```